K & D A/C Compressors' Business Card

Hello,

I need someone to create a new business card for my business. The name of my Business is: K & D A/C Compressors. I sell automotive air conditioning parts (a/c parts). I would like the business card to incorporate my logo, and to have an automotive feel to it. It is important that the business card feel like it is coming from an automotive parts business.

I already have a logo, which I will provide.

Thanks.
Updates

Project Deadline Extended Reason: I feel like extending the deadline until October 9, 2017, will allow for more time to design the business card. Thank you for your understanding. Added Monday, October 2, 2017

Target Market(s)

Consumers who need automotive a/c parts, and auto mechanics.

Industry/Entity Type

Automotive

Contact Information for Business Card

Business name: K & D A/C Compressors
Business Address: 48207 Southwest 36th Street, Bayside Heights, Florida 33190
Telephone: 305-472-1390
Fax: To be provided once I choose your design.
Website: www.kdcoolunits.example
Email: support@kdcoolunits.example
Names: To be provided once I choose your design.

Font styles to use
Sans Serif

Colors

Designer to choose colors to be used in the design.

Requirements
Must have
• The business card must include all of the "Business Card Details" and the logo I have uploaded.

```html
<!DOCTYPE html>
<html lang="en">
<head>
<meta charset="utf-8">
<title>K &amp; D A/C Compressors — Business Card</title>
<link rel="stylesheet" href="https://fonts.googleapis.com/css2?family=Montserrat:wght@300;400;500;600&display=swap">
<style>
  :root {
    --page: #ffffff;
    --card: #ffffff;
    --grey: #a7a8ab;
    --blue: #27aeea;
    --white: #ffffff;
  }
  * { margin: 0; padding: 0; box-sizing: border-box; }
  html, body {
    width: 1192px; height: 1200px; overflow: hidden;
    background: var(--page);
    font-family: "Montserrat", sans-serif;
  }
  .canvas { position: relative; width: 1192px; height: 1200px; }
  .card {
    position: absolute; width: 763px; height: 447px;
    background: var(--card); overflow: hidden;
    box-shadow: 0 6px 14px rgba(0,0,0,0.12);
  }
  .card--front { left: 136px; top: 118px; }
  .card--back { left: 299px; top: 634px; }
  .card__shapes { position: absolute; inset: 0; width: 100%; height: 100%; }

  .brand { position: absolute; color: var(--grey); line-height: 1; }
  .brand__row { display: flex; align-items: center; gap: 16px; }
  .brand__mark { width: 36px; height: 36px; background: var(--blue); }
  .brand__name { font-size: 64px; font-weight: 600; letter-spacing: 0; }
  .brand__sub { font-size: 30px; font-weight: 300; letter-spacing: 0.5px; margin-top: 6px; }
  .card--front .brand { left: 74px; top: 252px; }
  .card--back .brand { left: 45px; top: 46px; }

  .web-band {
    position: absolute; left: 399px; top: 256px; width: 364px; height: 94px;
    background: var(--grey); color: var(--white);
    font-size: 21px; font-weight: 400;
    display: flex; align-items: center; padding-left: 26px;
  }

  .person {
    position: absolute; left: 36px; top: 276px; color: var(--white);
    font-size: 22px; line-height: 31px;
  }
  .person__name { font-weight: 600; }
  .person__title { font-weight: 400; }

  .contact {
    position: absolute; right: 38px; top: 191px; text-align: right;
    color: var(--white); font-size: 20px; line-height: 28.5px; font-weight: 400;
  }
  .contact__block + .contact__block { margin-top: 28px; }
</style>
</head>
<body>
<div class="canvas">

  <section class="card card--front" aria-label="Business card front">
    <svg class="card__shapes" viewBox="0 0 763 447">
      <defs>
        <linearGradient id="dashTone" x1="0" y1="0" x2="0.3" y2="1">
          <stop offset="0" stop-color="#1d5f88"/>
          <stop offset="0.45" stop-color="#0f2f47"/>
          <stop offset="1" stop-color="#050b12"/>
        </linearGradient>
      </defs>
      <polygon points="0,0 71,0 0,220" fill="var(--grey)"/>
      <polygon points="492,0 763,0 763,447 385,447" fill="url(#dashTone)" role="img" aria-label="Photo of a car dashboard with glowing blue climate control dials"/>
    </svg>
    <div class="brand">
      <div class="brand__row"><span class="brand__mark"></span><span class="brand__name">K &amp; D</span></div>
      <div class="brand__sub">A/C Compressors</div>
    </div>
    <div class="web-band">www.kdcoolunits.example</div>
  </section>

  <section class="card card--back" aria-label="Business card back">
    <svg class="card__shapes" viewBox="0 0 763 447">
      <rect x="0" y="256" width="340" height="97" fill="var(--grey)"/>
      <polygon points="366,160 763,160 763,447 275,447" fill="var(--blue)"/>
    </svg>
    <div class="brand">
      <div class="brand__row"><span class="brand__mark"></span><span class="brand__name">K &amp; D</span></div>
      <div class="brand__sub">A/C Compressors</div>
    </div>
    <div class="person">
      <div class="person__name">Lorem Ipsum</div>
      <div class="person__title">Director</div>
    </div>
    <div class="contact">
      <div class="contact__block">P. 305-472-1390<br>F. 000-000-0000</div>
      <div class="contact__block">support@kdcoolunits.example</div>
      <div class="contact__block">48207 Southwest 36th Street,<br>Bayside Heights,<br>Florida 33190</div>
    </div>
  </section>

</div>
</body>
</html>
```